50 bday

It's my 50th bday and I need the invitation that we will be send by digital (mail and whatapp). One important aspect is that my bday is on day 2 month 2 of year 22 so this is going to be important things that I want to use it as the main theme as you can see in the attached example

```html
<!DOCTYPE html>
<html lang="es">
<head>
<meta charset="utf-8">
<title>Invitación 50 años</title>
<link href="https://fonts.googleapis.com/css2?family=Carlito:wght@400;700&display=swap" rel="stylesheet">
<style>
  :root {
    --page-grey: #cfcfcf;
    --night-teal: #045468;
    --night-deep: #011f2b;
    --accent-orange: #f07117;
    --blob-orange: #fe8530;
    --frame-orange: #f47a20;
    --gold: #d9b44a;
    --white: #ffffff;
  }
  * { margin: 0; padding: 0; box-sizing: border-box; }
  html, body {
    width: 1200px; height: 1200px; overflow: hidden;
    background: var(--page-grey);
    font-family: "Carlito", "Calibri", sans-serif;
  }
  .invitation {
    position: absolute; left: 89px; top: 294px;
    width: 1023px; height: 614px; overflow: hidden;
    background: radial-gradient(ellipse 420px 360px at 346px 253px, var(--night-teal), var(--night-deep));
  }
  .decor { position: absolute; inset: 0; width: 1023px; height: 614px; }
  .date {
    position: absolute; left: 108px; top: 150px;
    font-size: 113px; line-height: 1; color: var(--accent-orange);
    letter-spacing: 1px; white-space: nowrap;
  }
  .date-label {
    position: absolute; color: var(--white);
    font-size: 22.5px; white-space: nowrap;
  }
  .date-label--day { left: 107px; top: 280px; }
  .date-label--month { left: 270px; top: 277px; }
  .date-label--year { left: 384px; top: 274px; }
  .save-note {
    position: absolute; left: 118px; top: 405px; width: 422px;
    text-align: center; color: var(--white);
    font-size: 26.5px; line-height: 34px;
  }
  .bday-title {
    position: absolute; left: 638px; top: 510px;
    font-size: 68px; font-weight: 700; line-height: 1;
    color: var(--white); white-space: nowrap;
  }
</style>
</head>
<body>
<main class="invitation">
  <svg class="decor" viewBox="0 0 1023 614">
    <defs>
      <linearGradient id="portraitTones" x1="0" y1="0" x2="1" y2="1">
        <stop offset="0" stop-color="#c9d3dc"/>
        <stop offset="0.45" stop-color="#c89a84"/>
        <stop offset="0.75" stop-color="#9a9692"/>
        <stop offset="1" stop-color="#7f7c7a"/>
      </linearGradient>
      <linearGradient id="balloonTones" x1="0" y1="0" x2="1" y2="1">
        <stop offset="0" stop-color="#f1efe9"/>
        <stop offset="1" stop-color="#c9a868"/>
      </linearGradient>
      <radialGradient id="flourishTone">
        <stop offset="0" stop-color="#ffffff"/>
        <stop offset="1" stop-color="#ffffff" stop-opacity="0.55"/>
      </radialGradient>
      <radialGradient id="goldGlow" cx="0.3" cy="0.3" r="0.8">
        <stop offset="0" stop-color="#d9b44a" stop-opacity="0.35"/>
        <stop offset="1" stop-color="#d9b44a" stop-opacity="0.04"/>
      </radialGradient>
    </defs>

    <rect class="gold-ribbons-top" x="0" y="0" width="230" height="340" rx="24"
          fill="url(#goldGlow)" role="img" aria-label="Cintas doradas, destellos y confeti dorado"/>
    <rect class="gold-sparkles-top" x="760" y="0" width="190" height="70" rx="18"
          fill="url(#goldGlow)" role="img" aria-label="Destellos y puntos dorados"/>
    <rect class="gold-ribbons-bottom" x="90" y="540" width="175" height="74" rx="18"
          fill="url(#goldGlow)" role="img" aria-label="Cintas doradas con destello"/>

    <rect class="balloons" x="0" y="485" width="98" height="129" rx="40"
          fill="url(#balloonTones)" role="img" aria-label="Globos blancos y dorados con serpentinas"/>

    <g class="divider" stroke="var(--white)" stroke-width="1.6" fill="var(--white)">
      <line x1="127" y1="351" x2="234" y2="351"/>
      <line x1="427" y1="351" x2="534" y2="351"/>
      <circle cx="127" cy="351" r="3"/><circle cx="534" cy="351" r="3"/>
    </g>
    <rect class="divider-flourish" x="236" y="332" width="189" height="38" rx="19"
          fill="url(#flourishTone)" opacity="0.85" role="img" aria-label="Adorno de volutas blancas"/>

    <path class="orange-blob" fill="var(--blob-orange)"
          d="M1023,63 C900,63 760,110 680,220 C620,300 566,420 566,540 C566,570 568,595 573,614 L1023,614 Z"/>

    <rect class="photo-frame" x="605" y="79" width="378" height="402" fill="var(--frame-orange)"/>
    <rect class="photo-mat" x="615" y="89" width="358" height="382" fill="var(--white)"/>
    <text class="photo-numerals" x="638" y="448" textLength="312" lengthAdjust="spacingAndGlyphs"
          font-family="Carlito, sans-serif" font-weight="700" font-size="455"
          fill="url(#portraitTones)" role="img"
          aria-label="Fotografía del homenajeado sonriendo, recortada dentro del número 50">50</text>
  </svg>

  <div class="date">2 – 2- 22</div>
  <span class="date-label date-label--day">(dos)</span>
  <span class="date-label date-label--month">(febrero)</span>
  <span class="date-label date-label--year">(dos mil veintidos)</span>

  <p class="save-note">Reserva desde ahora ese día en tu agenda para juntos compartir en la celebración de mis 50 años</p>

  <h1 class="bday-title">50th bday</h1>
</main>
</body>
</html>
```